I need beautiful business cards with Moonpetals and sparrows on then and my tavolink business name is Moonpetals and sparrows.
I sell mini gardens, candles and melts and gift ware....on the other side I would like some thing like...REMEMBER to keep in touch with Moonpetals and sparrows buy a like,comment or just to say hello or tavo link will think you are no longer interested and delete you....you can change the wording to that to make smaller if you would like, and am not sure how to word it....my color theme for my business in purple and green. thank you.

tavo link:Moonpetals and sparrows
mini gardens
candles and melts
gift ware.
email:rosa514@kelvimail.com
phone:0873514062

```html
<!DOCTYPE html>
<html lang="en">
<head>
<meta charset="utf-8">
<title>Moonpetals and sparrows – business cards</title>
<link rel="stylesheet" href="https://fonts.googleapis.com/css2?family=Great+Vibes&family=Parisienne&family=Tinos&display=swap">
<style>
  :root {
    --page: #e8e6ea;
    --card-purple-top: #7d7689;
    --card-purple-bottom: #6f6878;
    --card-green-top: #79a585;
    --card-green-bottom: #5f8b6b;
    --ink: #ffffff;
    --shadow: rgba(0, 0, 0, 0.18);
  }
  * { margin: 0; padding: 0; box-sizing: border-box; }
  html, body {
    width: 1200px;
    height: 1000px;
    overflow: hidden;
    background: var(--page);
  }
  .sheet {
    position: relative;
    width: 1200px;
    height: 1000px;
  }
  .card {
    position: absolute;
    left: 190px;
    width: 820px;
    height: 470px;
    color: var(--ink);
    box-shadow: 0 6px 18px var(--shadow);
    overflow: hidden;
  }
  .card--front {
    top: 15px;
    background: linear-gradient(160deg, var(--card-green-top), var(--card-green-bottom));
  }
  .card--back {
    top: 515px;
    background: linear-gradient(160deg, var(--card-purple-top), var(--card-purple-bottom));
  }
  .rule {
    position: absolute;
    left: 0;
    width: 820px;
    height: 60px;
  }
  .rule svg { display: block; }
  .motif {
    fill: var(--ink);
    opacity: 0.9;
  }

  /* front */
  .front-rule-top { top: 40px; }
  .front-rule-bottom { top: 372px; }
  .brand {
    position: absolute;
    top: 92px;
    left: 0;
    width: 820px;
    text-align: center;
    font-family: "Great Vibes", cursive;
    font-weight: 400;
    line-height: 0.95;
  }
  .brand-main {
    display: block;
    font-size: 100px;
  }
  .brand-and {
    font-size: 36px;
    margin-left: 10px;
  }
  .brand-second {
    display: block;
    font-size: 100px;
    margin-left: 90px;
  }
  .tagline {
    position: absolute;
    top: 298px;
    left: 0;
    width: 820px;
    text-align: center;
    font-family: "Tinos", serif;
    font-size: 27px;
    letter-spacing: 0.3px;
  }
  .contact {
    position: absolute;
    top: 336px;
    left: 0;
    width: 820px;
    display: flex;
    justify-content: center;
    gap: 34px;
    font-family: "Tinos", serif;
    font-size: 27px;
  }
  .contact-item {
    display: flex;
    align-items: center;
    gap: 6px;
  }
  .contact-icon { display: block; }

  /* back */
  .back-rule-top { top: 62px; }
  .back-rule-bottom { top: 368px; }
  .message {
    position: absolute;
    top: 165px;
    left: 0;
    width: 820px;
    text-align: center;
    font-family: "Parisienne", cursive;
    font-size: 40px;
    line-height: 1.3;
  }
</style>
</head>
<body>
<main class="sheet">

  <section class="card card--front" aria-label="Front of business card">
    <div class="rule front-rule-top">
      <svg width="820" height="60" viewBox="0 0 820 60">
        <polygon fill="#fff" points="40,30 360,27 360,33"/>
        <polygon fill="#fff" points="780,30 460,27 460,33"/>
        <rect class="motif" x="380" y="12" width="60" height="36" rx="18" role="img" aria-label="Small white dragonfly silhouette"/>
      </svg>
    </div>

    <h1 class="brand">
      <span class="brand-main">Moonpetals<span class="brand-and">and</span></span>
      <span class="brand-second">sparrows</span>
    </h1>

    <p class="tagline">mini gardens, candles, and melts gift ware</p>

    <div class="contact">
      <span class="contact-item">
        <svg class="contact-icon" width="26" height="26" viewBox="0 0 26 26" aria-hidden="true">
          <circle cx="13" cy="13" r="11.5" fill="none" stroke="#fff" stroke-width="2"/>
          <path d="M9 7.5c-1.2 0.8-1.6 2.2-0.8 4.2 1.2 2.8 3.3 5 6 6.3 1.8 0.8 3.3 0.4 4.1-0.8l-2.3-2.1-1.5 1c-1.5-0.8-2.9-2.2-3.7-3.8l1-1.5z" fill="#fff"/>
        </svg>
        <span>0873514062</span>
      </span>
      <span class="contact-item">
        <svg class="contact-icon" width="26" height="26" viewBox="0 0 26 26" aria-hidden="true">
          <circle cx="13" cy="13" r="11.5" fill="none" stroke="#fff" stroke-width="2"/>
          <rect x="7" y="9" width="12" height="8.5" fill="none" stroke="#fff" stroke-width="1.6"/>
          <polyline points="7,9 13,14 19,9" fill="none" stroke="#fff" stroke-width="1.6"/>
        </svg>
        <span>rosa514@kelvimail.com</span>
      </span>
    </div>

    <div class="rule front-rule-bottom">
      <svg width="820" height="60" viewBox="0 0 820 60">
        <polygon fill="#fff" points="40,38 370,35 370,41"/>
        <polygon fill="#fff" points="780,38 450,35 450,41"/>
        <rect class="motif" x="382" y="14" width="56" height="44" rx="14" role="img" aria-label="Small white butterfly silhouette"/>
      </svg>
    </div>
  </section>

  <section class="card card--back" aria-label="Back of business card">
    <div class="rule back-rule-top">
      <svg width="820" height="60" viewBox="0 0 820 60">
        <polygon fill="#fff" points="60,30 370,27 370,33"/>
        <polygon fill="#fff" points="760,30 450,27 450,33"/>
        <rect class="motif" x="380" y="12" width="60" height="36" rx="18" role="img" aria-label="Small white dragonfly silhouette"/>
      </svg>
    </div>

    <p class="message">
      Remember to keep in touch with us<br>
      by liking our tavolink page.<br>
      Come visit anytime!
    </p>

    <div class="rule back-rule-bottom">
      <svg width="820" height="60" viewBox="0 0 820 60">
        <polygon fill="#fff" points="60,30 410,27 760,30 410,33"/>
      </svg>
    </div>
  </section>

</main>
</body>
</html>
```